Podcast cover art (not a logo)

I’m launching an audio-only podcast for parents of neurodivergent children. The podcast is meant to feel like a calm, trusted professional voice — not a brand or a performance.

Style direction:
--Clean and minimal
--Calm and grounded
--Professional, not playful
--Nothing flashy, loud, or busy
--No cartoon imagery

Content on the cover:
--Podcast title: Under the Quiet Surface
--Subtitle or tagline: Supporting Neurodivergent Kids with Science, Not Shame (or Understanding Neurodivergent Kids)
--No episode numbers, no dates

Design preferences:
--Text-forward design
--Neutral or soft colors (muted blues, grays, off-whites)
--High contrast for readability at small sizes
--Simple, timeless font

What I do NOT want:
--A logo or branding system
--Illustrations of children or families
--Bright colors or playful graphics
--Trendy fonts or visual effects

Technical requirements:
--Square image
--3000 × 3000 pixels
--RGB color mode
--JPEG or PNG
--File size under 500 KB

Deliverables:
--Final cover art file
--Optional: one or two alternate background color versions

```html
<!DOCTYPE html>
<html lang="en">
<head>
<meta charset="utf-8">
<title>Under the Quiet Surface — Podcast Cover</title>
<link href="https://fonts.googleapis.com/css2?family=Montserrat:wght@400;500&display=swap" rel="stylesheet">
<style>
  :root {
    --page-bg: #a4adb5;
    --cover-edge: #d8d8d8;
    --cover-mid: #e4e4e4;
    --cover-glow: #f2f2f2;
    --ink: #333333;
    --art-light: #f4f4f4;
    --art-mid: #dcdcdc;
  }
  * { margin: 0; padding: 0; box-sizing: border-box; }
  html, body {
    width: 1200px;
    height: 1082px;
    overflow: hidden;
    background: var(--page-bg);
  }
  .cover {
    position: absolute;
    left: 120px;
    top: 61px;
    width: 960px;
    height: 960px;
    background: radial-gradient(circle at 50% 52%, var(--cover-glow) 0%, var(--cover-mid) 45%, var(--cover-edge) 75%);
    font-family: "Montserrat", sans-serif;
    color: var(--ink);
    text-align: center;
  }
  .cover-art {
    position: absolute;
    left: 150px;
    top: 290px;
    width: 660px;
    height: 560px;
    border-radius: 46% 46% 38% 38%;
    background: radial-gradient(ellipse at 50% 65%, var(--art-light) 0%, var(--art-mid) 55%, rgba(220,220,220,0) 78%);
  }
  .title {
    position: absolute;
    left: 0;
    right: 0;
    top: 74px;
    font-weight: 400;
    line-height: 1;
  }
  .title span { display: block; }
  .title-top {
    font-size: 60px;
    letter-spacing: 0.42em;
    padding-left: 0.42em;
  }
  .title-middle {
    font-size: 38px;
    letter-spacing: 0.42em;
    padding-left: 0.42em;
    margin-top: 22px;
  }
  .title-bottom {
    font-size: 82px;
    letter-spacing: 0.36em;
    padding-left: 0.36em;
    margin-top: 20px;
  }
  .tagline {
    position: absolute;
    left: 0;
    right: 0;
    top: 850px;
    font-size: 22px;
    font-weight: 500;
    letter-spacing: 0.2em;
    line-height: 1.5;
  }
</style>
</head>
<body>
  <main class="cover">
    <div class="cover-art" role="img" aria-label="Soft grey misty shape with a small pale standing figure silhouette at its centre"></div>
    <h1 class="title">
      <span class="title-top">UNDER</span>
      <span class="title-middle">THE QUIET</span>
      <span class="title-bottom">SURFACE</span>
    </h1>
    <p class="tagline">Supporting Neurodivergent Kids with<br>Science, Not Shame</p>
  </main>
</body>
</html>
```